need professional, precise design for a website

I will start with a homepage design and if we pick your design, we'll have you design up to 6 more interior pages (we'll pay extra for these of course). We need a homepage design for a reserve study company based in Idaho, covering the northwest region. The company is called copper ridge reserve study. Their current site is at https://www.copperridgereserves.example/ and they really like this site for inspiration https://www.fundplannerhub.example/ but they would like an original design, just more modern and fresh like the sample site. I have logo files I will attach. They want something that looks financial and has a feel of accuity. Their main call to action will be to have someone fill in a contact form or call them on the phone. They will have a sample study that someone can download as on the fundplannerhub site. You can use copy from their current site.

```html
<!DOCTYPE html>
<html lang="en">
<head>
<meta charset="utf-8">
<title>Copper Ridge Reserves</title>
<link rel="stylesheet" href="https://fonts.googleapis.com/css2?family=Oswald:wght@300;400&family=Montserrat:wght@400;500;600&display=swap">
<style>
:root{
  --navy:#201c57;
  --tan:#bfa796;
  --tan-light:#e6dcd4;
  --white:#ffffff;
  --text-gray:#8a8a8a;
  --nav-gray:#6d6d6d;
  --copy-gray:#9a9a9a;
}
*{margin:0;padding:0;box-sizing:border-box}
html,body{width:712px;height:1200px;overflow:hidden;background:var(--white)}
body{position:relative;font-family:'Montserrat',sans-serif;color:var(--nav-gray)}
.abs{position:absolute}

/* top bar */
.top-bar{left:0;top:0;width:712px;height:31px;background:var(--navy)}
.top-phone{left:442px;top:10px;font-size:9.5px;color:#e8e6f2}
.top-phone b{font-weight:600;color:var(--white);margin-right:3px}
.social{top:5px;width:22px;height:21px;border-radius:2px}
.social.s1{left:561px;background:#3b5594}
.social.s2{left:589px;background:#1da1e6}
.social.s3{left:617px;background:#d8402d}
.social.s4{left:645px;background:#0d74b8}

/* header */
.site-header{left:0;top:31px;width:712px;height:93px;background:var(--white)}
.brand{left:47px;top:57px;display:flex;align-items:center;gap:9px}
.brand-mark{width:26px;height:26px;border-radius:50%;background:var(--navy)}
.brand-name{font-family:'Oswald',sans-serif;font-weight:400;font-size:22px;letter-spacing:.5px;color:var(--navy);text-transform:uppercase}
.quote-btn{left:561px;top:43px;width:105px;height:31px;background:var(--tan);color:var(--white);font-size:11px;font-weight:500;display:flex;align-items:center;justify-content:center}
.main-nav{top:87px;font-family:'Oswald',sans-serif;font-weight:300;font-size:12.5px;color:var(--nav-gray)}
.main-nav.active{color:var(--tan)}
.nav-caret{left:374px;top:104px}
.search-icon{left:652px;top:88px}

/* accent strip */
.accent-strip{left:0;top:124px;width:712px;height:6px;background:var(--tan)}
.strip-caret{left:344px;top:129px}

/* hero */
.hero{left:0;top:130px;width:712px;height:340px;background:linear-gradient(180deg,#6f7a86 0%,#8a8f93 35%,#6b6a5e 62%,#4c5a3e 80%,#3e4533 100%)}
.hero-shade{left:0;top:130px;width:712px;height:340px;background:rgba(30,28,50,.28)}
.hero-title{left:0;top:230px;width:712px;text-align:center;font-family:'Oswald',sans-serif;font-weight:400;font-size:38px;color:var(--white);letter-spacing:.3px}
.hero-text{left:186px;top:289px;width:340px;text-align:center;font-size:10.6px;line-height:18.5px;color:var(--white)}
.pill-btn{height:31px;border-radius:16px;background:var(--tan-light);box-shadow:4px 0 0 var(--tan),-4px 0 0 var(--tan);color:#3a3a3a;font-size:11px;font-weight:500;display:flex;align-items:center;justify-content:center}
.hero-btn{left:314px;top:340px;width:84px}
.hero-arrow{top:291px;width:31px;height:31px;border-radius:50%}
.hero-arrow.prev{left:31px;background:rgba(255,255,255,.35)}
.hero-arrow.next{left:651px;border:1.5px solid rgba(255,255,255,.8)}

/* services */
.services{left:0;top:470px;width:712px;height:235px;background:var(--navy)}
.service-card{top:507px;width:161px;height:161px;background:var(--tan)}
.service-icon{left:48px;top:14px;width:65px;height:70px;background:rgba(255,255,255,.2);border-radius:2px}
.service-title{left:0;top:110px;width:161px;text-align:center;font-family:'Oswald',sans-serif;font-weight:300;font-size:14px;line-height:19px;color:var(--white)}

/* about */
.about-title{left:47px;top:736px;font-family:'Oswald',sans-serif;font-weight:400;font-size:24px;color:var(--navy)}
.about-sub{left:47px;top:775px;font-family:'Oswald',sans-serif;font-weight:300;font-style:italic;font-size:15px;color:#2c2c2c}
.about-text{left:47px;top:802px;width:308px;font-size:8.6px;line-height:15.5px;color:var(--text-gray)}
.about-btn{left:51px;top:897px;width:84px}
.video{left:388px;top:742px;width:278px;height:186px;background:linear-gradient(135deg,#6f6f9e 0%,#5a5b8c 55%,#4b4d7c 100%)}
.play{left:502px;top:808px}

/* footer */
.footer{left:0;top:971px;width:712px;height:186px;background:var(--tan)}
.footer-title{left:47px;top:996px;font-family:'Oswald',sans-serif;font-weight:300;font-size:19px;color:var(--white)}
.footer-text{left:47px;top:1031px;font-size:9.6px;line-height:16px;color:var(--white)}
.footer-contact{left:47px;font-size:9.6px;color:var(--white)}
.footer-contact b{display:inline-block;width:43px;font-weight:600}
.subscribe{left:345px;top:1002px;width:321px;height:102px;border:3px solid var(--white)}
.subscribe-title{left:0;top:15px;width:315px;text-align:center;font-size:14.5px;color:var(--white)}
.email-field{left:14px;top:46px;width:186px;height:34px;background:var(--white);font-size:9px;color:#777;padding-left:10px;display:flex;align-items:center}
.subscribe-btn{left:205px;top:46px;width:96px;height:34px;border:1.5px solid var(--white);color:var(--white);font-size:11px;display:flex;align-items:center;justify-content:center}

.copyright{left:0;top:1175px;width:712px;text-align:center;font-size:8.6px;color:var(--copy-gray)}
.copyright span{color:var(--tan);font-weight:600}
</style>
</head>
<body>

<div class="abs top-bar"></div>
<div class="abs top-phone"><b>Phone :</b> (208) 555-0142</div>
<div class="abs social s1" aria-label="Social link"></div>
<div class="abs social s2" aria-label="Social link"></div>
<div class="abs social s3" aria-label="Social link"></div>
<div class="abs social s4" aria-label="Social link"></div>

<header class="abs site-header"></header>
<div class="abs brand"><span class="brand-mark"></span><span class="brand-name">Copper Ridge Reserves</span></div>
<div class="abs quote-btn">Request a quote</div>
<div class="abs main-nav active" style="left:366px">Home</div>
<div class="abs main-nav" style="left:409px">About Our Company</div>
<div class="abs main-nav" style="left:514px">Reserve Studies</div>
<div class="abs main-nav" style="left:601px">Contact</div>
<svg class="abs nav-caret" width="9" height="8" viewBox="0 0 9 8"><path d="M4.5 0L9 8H0z" fill="var(--tan)"/></svg>
<svg class="abs search-icon" width="13" height="13" viewBox="0 0 13 13"><circle cx="5.5" cy="5.5" r="4.3" fill="none" stroke="#444" stroke-width="1.4"/><path d="M8.6 8.6L12.3 12.3" stroke="#444" stroke-width="1.5"/></svg>

<div class="abs accent-strip"></div>

<div class="abs hero" role="img" aria-label="Photo of a suburban street with houses and autumn trees"></div>
<div class="abs hero-shade"></div>
<svg class="abs strip-caret" width="24" height="12" viewBox="0 0 24 12"><path d="M0 0H24L12 12z" fill="var(--tan)"/></svg>
<h1 class="abs hero-title">ABOUT COPPER RIDGE RESERVES</h1>
<p class="abs hero-text">Lorem ipsum dolor sit amet, consectetur adipiscing elit, sed do eiusmod tempor incididunt ut labore et dolore magna aliqua.</p>
<div class="abs pill-btn hero-btn">Read More</div>
<div class="abs hero-arrow prev"><svg width="31" height="31" viewBox="0 0 31 31"><path d="M17 11l-5 4.5 5 4.5" fill="none" stroke="#fff" stroke-width="2"/></svg></div>
<div class="abs hero-arrow next"><svg width="28" height="28" viewBox="0 0 28 28"><path d="M12 9.5l5 4.5-5 4.5" fill="none" stroke="#fff" stroke-width="2"/></svg></div>

<section class="abs services"></section>
<div class="abs service-card" style="left:90px">
  <div class="abs service-icon" role="img" aria-label="Line icon of condominium towers"></div>
  <div class="abs service-title">HOA &amp; Condominium<br>Studies</div>
</div>
<div class="abs service-card" style="left:276px">
  <div class="abs service-icon" role="img" aria-label="Line icon of commercial building with shield"></div>
  <div class="abs service-title">Commercial, Vacation &amp;<br>Time Share</div>
</div>
<div class="abs service-card" style="left:461px">
  <div class="abs service-icon" role="img" aria-label="Line icon of tree, bench and sun"></div>
  <div class="abs service-title">Parks &amp; Public<br>Lands</div>
</div>

<h2 class="abs about-title">ABOUT COPPER RIDGE RESERVES</h2>
<p class="abs about-sub">Your financial road map for the next 30 years!</p>
<p class="abs about-text">The ridgeline is a constant on the horizon that travelers have relied on for centuries. &nbsp;Navigating by it is simply knowing the right points of origin and following the map that the land has laid before us. We love the high country! &nbsp;Amidst so much rough terrain and a seemingly chaotic expanse of peaks and valleys, there is great order.</p>
<div class="abs pill-btn about-btn">Read More</div>
<div class="abs video" role="img" aria-label="Video still of a business meeting at an office desk"></div>
<svg class="abs play" width="72" height="52" viewBox="0 0 72 52"><circle cx="36" cy="26" r="24" fill="rgba(255,255,255,.35)" stroke="#fff" stroke-width="3"/><path d="M31 16v20l15-10z" fill="#fff"/></svg>

<footer class="abs footer"></footer>
<div class="abs footer-title">Copper Ridge Reserves, LLC</div>
<p class="abs footer-text">Serving Idaho, Montana, Oregon,<br>Utah, Washington &amp; Wyoming</p>
<div class="abs footer-contact" style="top:1074px"><b>Phone :</b>(208) 555-0142</div>
<div class="abs footer-contact" style="top:1092px"><b>Email :</b>Dana@CopperRidgeReserves.example</div>
<div class="abs subscribe">
  <div class="abs subscribe-title">Receive important information &amp; updates</div>
  <div class="abs email-field">Enter Email Address...</div>
  <div class="abs subscribe-btn">Subscribe</div>
</div>

<p class="abs copyright">Copyright <span>Copper Ridge Reserves, LLC</span> © 2017 All Rights Reserved</p>

</body>
</html>
```